BRAMLEIGH real estate family office

Hello, Our business is a real estate intermediation activity on high-end goods (amounts exceeding € 10m) for corporate and private clients. You can see our logo on the site www.bramleigh-invented.fr We would like to keep that spirit with the hexagon that represents France (transactions between Monaco and Saint Tropez, Courchevel and Paris). And the "baseline" that is "real estate family office". The corporate logo should be and can be printed by embossing (relief). We must integrate the name, first name, phone, email and website. Finally, to imbibe the spirit of business, here is a detail of the activity. "Genuine consulting firm in real estate investments, BRAMLEIGH works with its customers as a specialized player in the high-end markets, we are recognized for our ultra-confidential approach and tailor-made, as well as the quality of our network. We broadcast any information on the market and we work exclusively through a strong relationship we have developed over the years. BRAMLEIGH is active on the French Riviera (from Monaco to Saint-Tropez), the Alps (Courchevel, Méribel, Megève) and Paris (essentially market premium). Always looking for opportunities for our clients, we work on two investment areas: residential luxury real estate (properties, vineyards, mansions, land, etc.) commercial real estate (empty office buildings or yield, hotel properties, land, etc.) "

Target Market(s)

High foreign end customers. corporate and private.

Industry/Entity Type

Real Estate

Contact Information for Business Card

LOGO
baseline
Laurent Dufossé
+33(0)6.41.57.09.64
ld@bramleigh-invented.fr
www.bramleigh-invented.fr

Font styles to use
Serif

Colors
cedeed
0255a3
3277b5
85abd2
85cae6
34a7d7
0792cd
cfdeed
1b1b1b

Requirements
Must have
• see description

```html
<!DOCTYPE html>
<html lang="fr">
<head>
<meta charset="utf-8">
<title>BRAMLEIGH – business card</title>
<link rel="stylesheet" href="https://fonts.googleapis.com/css2?family=Poppins:wght@300;400;600&family=Tinos&display=swap">
<style>
  :root {
    --page-bg: #2b2b2d;
    --card-white: #ffffff;
    --card-grey: #6b6c6f;
    --slate: #5c5d61;
    --rule-grey: #8a8b8e;
    --brand-blue: #1d3aa6;
    --accent-blue: #3a55b8;
    --ink: #3e3f42;
  }
  html, body {
    margin: 0;
    padding: 0;
    width: 1200px;
    height: 900px;
    overflow: hidden;
    background: var(--page-bg);
  }
  .canvas {
    position: relative;
    width: 1200px;
    height: 900px;
  }
  .card {
    position: absolute;
    width: 600px;
    height: 343px;
    border-radius: 18px;
    overflow: hidden;
  }

  /* Back side */
  .card-back {
    left: 130px;
    top: 70px;
    background: var(--card-grey);
  }
  .card-back .wordmark {
    position: absolute;
    left: 0;
    right: 0;
    top: 132px;
    text-align: center;
    font-family: "Poppins", sans-serif;
    font-weight: 300;
    font-size: 46px;
    letter-spacing: 6px;
    color: var(--card-white);
  }
  .card-back .web {
    position: absolute;
    right: 150px;
    bottom: 34px;
    font-family: "Poppins", sans-serif;
    font-size: 15px;
    color: var(--card-white);
  }
  .card-back .web b { font-weight: 600; }
  .card-back .base-band {
    position: absolute;
    left: 0;
    bottom: 0;
    width: 330px;
    height: 10px;
    background: var(--card-white);
  }
  .card-back .base-tick {
    position: absolute;
    left: 330px;
    bottom: 10px;
    width: 6px;
    height: 14px;
    background: var(--card-white);
  }

  /* Front side */
  .card-front {
    left: 470px;
    top: 480px;
    background: var(--card-white);
  }
  .logo {
    position: absolute;
    left: 40px;
    top: 58px;
    display: inline-block;
    text-align: right;
    font-family: "Poppins", sans-serif;
  }
  .logo .wordmark {
    font-weight: 300;
    font-size: 40px;
    letter-spacing: 4px;
    color: var(--slate);
    line-height: 1;
    white-space: nowrap;
  }
  .logo .baseline {
    margin-top: 4px;
    margin-right: 4px;
    font-size: 13px;
    letter-spacing: 1px;
    line-height: 1.2;
    color: var(--accent-blue);
    white-space: nowrap;
  }
  .holder-name {
    position: absolute;
    right: 40px;
    top: 144px;
    font-family: "Tinos", serif;
    font-size: 27px;
    line-height: 1.2;
    color: var(--brand-blue);
    text-transform: uppercase;
    letter-spacing: 0.5px;
    white-space: nowrap;
  }
  .name-rule {
    position: absolute;
    left: 300px;
    right: 20px;
    top: 180px;
    height: 2px;
    background: var(--rule-grey);
  }
  .corner-block {
    position: absolute;
    right: 0;
    top: 160px;
    width: 20px;
    height: 22px;
    background: var(--card-grey);
  }
  .contact-rule {
    position: absolute;
    left: 40px;
    width: 340px;
    top: 236px;
    height: 2px;
    background: var(--rule-grey);
  }
  .contact-band {
    position: absolute;
    left: 380px;
    right: 0;
    top: 222px;
    height: 16px;
    background: var(--card-grey);
  }
  .contact-list {
    position: absolute;
    left: 40px;
    top: 245px;
    margin: 0;
    padding: 0;
    list-style: none;
    font-family: "Poppins", sans-serif;
    font-size: 15px;
    color: var(--ink);
  }
  .contact-list li {
    display: flex;
    align-items: center;
    gap: 12px;
    height: 24px;
  }
  .contact-list svg { width: 13px; height: 13px; flex: none; }
  .contact-list b { color: var(--brand-blue); font-weight: 600; }
  .footer-band {
    position: absolute;
    left: 0;
    bottom: 0;
    width: 330px;
    height: 12px;
    background: var(--brand-blue);
  }
</style>
</head>
<body>
<main class="canvas">

  <section class="card card-back" aria-label="Card back">
    <div class="wordmark">BRAMLEIGH</div>
    <div class="web">www.<b>bramleigh-invented</b>.fr</div>
    <div class="base-band"></div>
    <div class="base-tick"></div>
  </section>

  <section class="card card-front" aria-label="Card front">
    <div class="logo">
      <div class="wordmark">BRAMLEIGH</div>
      <div class="baseline">real estate family office</div>
    </div>

    <div class="holder-name">Laurent Dufossé</div>
    <div class="name-rule"></div>
    <div class="corner-block"></div>

    <div class="contact-rule"></div>
    <div class="contact-band"></div>

    <ul class="contact-list">
      <li>
        <svg viewBox="0 0 16 16" aria-hidden="true"><path fill="#1d3aa6" d="M3.6 1.2l2.3 2.6-1.3 1.8c.8 1.9 2.2 3.3 4 4.1l1.8-1.3 2.6 2.3-1.2 2.3C6.6 13 3 9.4 1.3 4.4z"/></svg>
        <span>+33(0)6.41.57.09.64</span>
      </li>
      <li>
        <svg viewBox="0 0 16 16" aria-hidden="true"><rect x="1" y="3" width="14" height="10" rx="1" fill="none" stroke="#1d3aa6" stroke-width="1.6"/><path d="M1.5 3.8L8 9l6.5-5.2" fill="none" stroke="#1d3aa6" stroke-width="1.6"/></svg>
        <span>ld@bramleigh-invented.fr</span>
      </li>
      <li>
        <svg viewBox="0 0 16 16" aria-hidden="true"><circle cx="8" cy="8" r="6.5" fill="none" stroke="#1d3aa6" stroke-width="1.4"/><ellipse cx="8" cy="8" rx="2.8" ry="6.5" fill="none" stroke="#1d3aa6" stroke-width="1.2"/><path d="M1.5 8h13M2.5 5h11M2.5 11h11" stroke="#1d3aa6" stroke-width="1"/></svg>
        <span>www.<b>bramleigh-invented</b>.fr</span>
      </li>
    </ul>

    <div class="footer-band"></div>
  </section>

</main>
</body>
</html>
```